business card for LWR pty ltd

We require a business card that stands out . I have included our company flyer and would like the services listed to be put on the card so when we Give out the cards to customers they have an idea of services we provide. need the winning design to be in editable photo shop format, editable iMac pages format or editable windows publisher format, so that I can enter in names, email addresses, phone numbers etc myself. I have included a pdf documents of info / items needed on the card to use as reference please.
Updates

need more submissions

Need extra days to review

Sick

Target Market(s)

new customers

Contact Information for Business Card

details are on attached business card requirements file

Requirements
Must have
• I have attached a list of must haves

```html
<!DOCTYPE html>
<html lang="en">
<head>
<meta charset="utf-8">
<title>LWR pty ltd – Business Card</title>
<link href="https://fonts.googleapis.com/css2?family=Roboto+Condensed:wght@400;700&family=Roboto:wght@400;700;900&display=swap" rel="stylesheet">
<style>
  :root{
    --page:#e9e7e3;
    --card-dark:#151515;
    --card-mid:#2a2a2a;
    --red:#e42126;
    --red-dark:#b5161a;
    --white:#ffffff;
    --grey-light:#d9d9d9;
    --grey-text:#cfcfcf;
    --ink:#1a1a1a;
  }
  *{margin:0;padding:0;box-sizing:border-box}
  html,body{width:900px;height:1200px;overflow:hidden;background:var(--page)}
  body{position:relative;font-family:"Roboto",Arial,sans-serif}

  .card{position:absolute;left:60px;width:780px;height:445px;overflow:hidden;
        background:linear-gradient(160deg,var(--card-mid) 0%,var(--card-dark) 60%);
        box-shadow:0 6px 18px rgba(0,0,0,.25)}
  .card--front{top:110px}
  .card--back{top:625px}

  /* FRONT */
  .brand{position:absolute;top:22px;left:0;width:100%;text-align:center;
         font-family:"Roboto",Arial,sans-serif;font-weight:900;font-size:74px;
         letter-spacing:6px;color:var(--grey-light);line-height:1}
  .front-photo{position:absolute;left:0;top:110px;width:100%;height:175px;
        background:linear-gradient(180deg,#8aa0b4 0%,#c9b49a 45%,#b8643a 75%,#151515 100%)}
  .company{position:absolute;left:34px;top:296px;font-family:"Roboto Condensed",Arial,sans-serif;
        font-weight:700;font-size:36px;color:var(--white);letter-spacing:1px}
  .phone-box{position:absolute;right:0;top:290px;width:340px;height:44px;background:var(--red);
        display:flex;align-items:center;padding-left:22px;gap:14px;color:var(--white);
        font-family:"Roboto Condensed",Arial,sans-serif;font-weight:700;font-size:32px}
  .phone-box svg{width:24px;height:24px}
  .person{position:absolute;left:34px;top:342px;font-family:"Roboto Condensed",Arial,sans-serif}
  .person__name{font-weight:700;font-size:24px;color:var(--white);letter-spacing:.5px}
  .person__role{font-weight:700;font-size:17px;color:var(--red);letter-spacing:1px}
  .contact{position:absolute;left:456px;top:342px;font-size:16px;color:var(--white);line-height:25px}
  .contact li{list-style:none;display:flex;align-items:center;gap:8px}
  .contact svg{width:15px;height:15px}
  .address-bar{position:absolute;left:0;bottom:18px;width:100%;height:34px;background:var(--grey-light);
        display:flex;align-items:center;padding-left:34px;font-family:"Roboto Condensed",Arial,sans-serif;
        font-weight:700;font-size:16px;color:var(--ink);letter-spacing:.5px}

  /* BACK */
  .services-tab{position:absolute;top:0;right:0;width:430px;height:62px}
  .services-tab__label{position:absolute;top:14px;left:96px;font-family:"Roboto Condensed",Arial,sans-serif;
        font-weight:700;font-size:28px;color:var(--white);letter-spacing:1px}
  .back-photo{position:absolute;left:0;top:120px;width:470px;height:225px;
        background:linear-gradient(180deg,#9fb3c6 0%,#d6d2c8 40%,#8a8a86 75%,#1f1f1f 100%)}
  .phone-pill{position:absolute;left:46px;top:365px;width:240px;height:46px;border-radius:23px;
        background:var(--white);display:flex;align-items:center;gap:12px;padding-left:4px;
        font-family:"Roboto Condensed",Arial,sans-serif;font-weight:700;font-size:28px;color:var(--ink)}
  .phone-pill__icon{width:38px;height:38px;border-radius:50%;background:var(--red);display:flex;align-items:center;justify-content:center}
  .phone-pill__icon svg{width:20px;height:20px}
  .service-list{position:absolute;left:500px;top:82px;list-style:none;
        font-weight:700;font-size:16.5px;color:var(--white);line-height:20.5px}
  .service-list li{position:relative;padding-left:16px}
  .service-list li::before{content:"";position:absolute;left:0;top:7px;width:7px;height:7px;background:var(--red)}
  .service-note{position:absolute;left:500px;top:355px;width:170px;font-size:12.5px;line-height:15px;
        font-weight:700;color:var(--red)}
</style>
</head>
<body>

<section class="card card--front" aria-label="Business card front">
  <div class="brand">LWR</div>
  <div class="front-photo" role="img" aria-label="Road train trucks with side tippers on an outback road"></div>
  <div class="company">LWR PTY LTD</div>
  <div class="phone-box">
    <svg viewBox="0 0 24 24" fill="#fff"><path d="M6.6 10.8a15.1 15.1 0 0 0 6.6 6.6l2.2-2.2a1 1 0 0 1 1-.25 11.4 11.4 0 0 0 3.6.57 1 1 0 0 1 1 1V20a1 1 0 0 1-1 1A17 17 0 0 1 3 4a1 1 0 0 1 1-1h3.5a1 1 0 0 1 1 1c0 1.25.2 2.45.57 3.57a1 1 0 0 1-.25 1z"/></svg>
    <span>000 444 000</span>
  </div>
  <div class="person">
    <div class="person__name">DANIEL HART</div>
    <div class="person__role">DIRECTOR</div>
  </div>
  <ul class="contact">
    <li><svg viewBox="0 0 24 24" fill="#e42126"><path d="M2 5h20v14H2z"/><path d="M2 5l10 8 10-8" stroke="#fff" stroke-width="1.6" fill="none"/></svg>email@lwrhaulage.com.au</li>
    <li><svg viewBox="0 0 24 24" fill="none" stroke="#e42126" stroke-width="2.2"><circle cx="12" cy="12" r="9"/><path d="M3 12h18M12 3c3 3.5 3 14.5 0 18M12 3c-3 3.5-3 14.5 0 18"/></svg>www.websiteaddress.com</li>
  </ul>
  <div class="address-bar">DEPOT : LWR LOT 114, TWELVE MILE ROAD, RED FLATS, AUSTRALIA</div>
</section>

<section class="card card--back" aria-label="Business card back">
  <svg class="services-tab" viewBox="0 0 430 62" preserveAspectRatio="none">
    <path d="M40 0H430V62H80Q58 62 50 40Z" fill="#e42126"/>
    <path d="M0 0H40Q50 40 80 62H60Q30 50 20 0Z" fill="#b5161a"/>
  </svg>
  <div class="services-tab__label" style="right:auto;left:auto;top:14px;position:absolute;margin-left:0;transform:translateX(0);" ></div>
  <div class="services-tab__label" style="left:446px">OUR SERVICES</div>

  <div class="back-photo" role="img" aria-label="Prime mover carrying a loader on a float trailer"></div>

  <div class="phone-pill">
    <span class="phone-pill__icon"><svg viewBox="0 0 24 24" fill="#fff"><path d="M6.6 10.8a15.1 15.1 0 0 0 6.6 6.6l2.2-2.2a1 1 0 0 1 1-.25 11.4 11.4 0 0 0 3.6.57 1 1 0 0 1 1 1V20a1 1 0 0 1-1 1A17 17 0 0 1 3 4a1 1 0 0 1 1-1h3.5a1 1 0 0 1 1 1c0 1.25.2 2.45.57 3.57a1 1 0 0 1-.25 1z"/></svg></span>
    <span>000 444 000</span>
  </div>

  <ul class="service-list">
    <li>Over Size Loads/Hot Shot Loads</li>
    <li>Heavy Vehicle Recovery Services</li>
    <li>Potable Water Deliveries</li>
    <li>Road Building/Maintenance</li>
    <li>Earthworks</li>
    <li>Sand &amp; Metal Supply &amp; Cartage</li>
    <li>Road Train Tippers</li>
    <li>Road Train Tankers</li>
    <li>Road Train Flat Tops</li>
    <li>Drop Deck Trailers</li>
    <li>Mine Site Accredited</li>
    <li>Equipment &amp; Operators</li>
  </ul>
  <p class="service-note">We offer a large range of services not listed so call us today for a personalised quote to suit your needs.</p>
</section>

</body>
</html>
```